11 x 11 Flyer Design for Social Media - Reverse Mortgages

62 or older?

A Reverse Mortgage
could be
Your Road to Financial Freedom

* No Monthly Payments
* No Income Requirements
* No Credit Score Requirements
* No Loss of Ownership

Receive cash by lump sum, monthly installments or a line of credit!!

Call us today for a Free Consultation!!
(800) 471-2965

Bluegate Financial Services, Inc.
NMLS #318760
www.bluegatehome.com

```html
<!DOCTYPE html>
<html lang="en">
<head>
<meta charset="utf-8">
<title>Reverse Mortgage Flyer – Bluegate Financial Services</title>
<link href="https://fonts.googleapis.com/css2?family=Poppins:wght@400;500;600;700;800&display=swap" rel="stylesheet">
<style>
  :root {
    --navy: #11508f;
    --teal: #0b7896;
    --teal-deep: #0a6a86;
    --sky: #1a96d4;
    --lime: #9ccf4c;
    --lime-soft: #c3dd7b;
    --mist: #e9e8ec;
    --slate: #6f7477;
    --white: #ffffff;
    --stage: #ececec;
  }
  * { box-sizing: border-box; margin: 0; padding: 0; }
  html, body { width: 1200px; height: 789px; overflow: hidden; }
  body { background: var(--stage); font-family: "Poppins", sans-serif; position: relative; }

  .flyer {
    position: absolute; left: 230px; top: 24px;
    width: 740px; height: 740px;
    background: var(--white);
    box-shadow: 0 10px 30px rgba(0,0,0,.18);
    overflow: hidden;
  }
  .flyer-shapes { position: absolute; inset: 0; width: 740px; height: 740px; }

  .abs { position: absolute; }

  .brand { left: 40px; top: 42px; display: flex; align-items: center; gap: 10px; }
  .brand-mark { width: 22px; height: 22px; background: var(--navy); border-radius: 50%; }
  .brand-name { color: var(--navy); font-weight: 600; font-size: 17px; line-height: 1.2; width: 220px; }

  .age-question { left: 58px; top: 150px; color: var(--white); line-height: .95; }
  .age-question .age-number { color: var(--lime); font-weight: 800; font-size: 60px; }
  .age-question .age-or { font-weight: 700; font-size: 56px; }
  .age-question .age-older { display: block; font-weight: 400; font-size: 54px; }

  .headline { left: 430px; top: 258px; width: 300px; text-align: center; color: var(--navy); }
  .headline-title { font-weight: 700; font-size: 27px; line-height: 1.2; }
  .headline-sub { font-weight: 500; font-size: 15.5px; line-height: 1.25; margin-top: 4px; }

  .benefits { right: 42px; top: 366px; list-style: none; text-align: right; color: var(--white); }
  .benefits li { font-weight: 600; font-size: 19.5px; line-height: 30px; }
  .benefit-rail { right: 22px; top: 372px; }

  .cash-tag { left: 232px; top: 530px; background: var(--lime); color: var(--navy);
    font-weight: 600; font-size: 17px; padding: 6px 14px; }
  .cash-dash { left: 436px; top: 544px; width: 12px; height: 4px; background: var(--navy); }

  .payout-list { left: 470px; top: 508px; list-style: none; }
  .payout-list li { display: flex; align-items: center; gap: 12px; height: 52px;
    color: var(--navy); font-weight: 600; font-size: 19px; }
  .payout-icon { width: 32px; height: 32px; border-radius: 7px; background: var(--navy);
    display: flex; align-items: center; justify-content: center; flex: none; }
  .payout-rail { left: 485px; top: 540px; width: 3px; height: 92px; background: var(--navy); }

  .cta-tag { left: 62px; top: 588px; background: var(--navy); color: var(--white);
    font-weight: 800; font-size: 22px; padding: 0 10px; line-height: 34px; }
  .cta-note { left: 62px; top: 630px; color: var(--navy); font-weight: 500; font-size: 15px; }
  .cta-phone { left: 30px; top: 662px; display: flex; align-items: center; gap: 10px;
    color: var(--navy); font-weight: 700; font-size: 38px; letter-spacing: .5px; }

  .contact { left: 480px; top: 668px; color: var(--white); font-size: 12.5px; line-height: 1.35; }
  .contact-row { display: flex; gap: 8px; align-items: flex-start; margin-bottom: 5px; }
  .contact-row svg { flex: none; margin-top: 1px; }
</style>
</head>
<body>
<div class="flyer">
  <svg class="flyer-shapes" viewBox="0 0 740 740" aria-hidden="false">
    <!-- background panels -->
    <polygon points="0,215 50,290 330,290 0,600" fill="var(--teal)"/>
    <polygon points="330,345 740,345 740,495 210,495" fill="var(--teal-deep)"/>
    <polygon points="210,495 740,495 740,660 420,660 440,740 0,740 0,600" fill="var(--mist)"/>
    <polygon points="420,660 740,660 740,740 440,740" fill="var(--teal)"/>
    <polygon points="0,575 400,575 440,740 0,740" fill="var(--lime-soft)"/>
    <polygon points="0,575 180,575 110,740 0,740" fill="var(--lime)"/>
    <polygon points="430,250 740,250 740,345 330,345" fill="var(--lime)"/>

    <g role="img" aria-label="Photo: senior couple laughing together, tinted blue">
      <polygon points="345,0 740,0 740,250 430,250 330,290 230,130" fill="url(#skyTint)"/>
    </g>
    <g role="img" aria-label="Photo: thoughtful senior man, grey tinted">
      <polygon points="0,130 230,130 330,290 50,290 0,215" fill="url(#greyTint)"/>
    </g>
    <g role="img" aria-label="Photo: smiling senior couple in a convertible car">
      <polygon points="110,292 326,292 168,452 0,452 0,400" fill="url(#carTone)"/>
    </g>
    <g role="img" aria-label="Photo: happy senior couple taking a selfie by the water">
      <polygon points="0,456 164,456 58,572 0,572" fill="url(#waterTone)"/>
    </g>

    <defs>
      <linearGradient id="skyTint" x1="0" y1="0" x2="1" y2="1">
        <stop offset="0" stop-color="#1aa0dc"/><stop offset="1" stop-color="#1380c4"/>
      </linearGradient>
      <linearGradient id="greyTint" x1="0" y1="0" x2="1" y2="0">
        <stop offset="0" stop-color="#7b7f82"/><stop offset="1" stop-color="#5f6366"/>
      </linearGradient>
      <linearGradient id="carTone" x1="0" y1="0" x2="1" y2="1">
        <stop offset="0" stop-color="#8f8b7a"/><stop offset=".6" stop-color="#6b6458"/><stop offset="1" stop-color="#9aa7b8"/>
      </linearGradient>
      <linearGradient id="waterTone" x1="0" y1="0" x2="1" y2="1">
        <stop offset="0" stop-color="#6d9ec8"/><stop offset="1" stop-color="#3a4a5c"/>
      </linearGradient>
    </defs>
  </svg>

  <div class="abs brand">
    <span class="brand-mark"></span>
    <span class="brand-name">Bluegate Financial Services, Inc.</span>
  </div>

  <h1 class="abs age-question">
    <span class="age-number">62</span> <span class="age-or">or</span>
    <span class="age-older">older?</span>
  </h1>

  <div class="abs headline">
    <p class="headline-title">A Reverse Mortgage</p>
    <p class="headline-sub">could be Your Road to Financial Freedom</p>
  </div>

  <ul class="abs benefits">
    <li>No Monthly Payments</li>
    <li>No Income Requirements</li>
    <li>No Credit Score Requirements</li>
    <li>No Loss of Ownership</li>
  </ul>
  <svg class="abs benefit-rail" width="8" height="106" viewBox="0 0 8 106" aria-hidden="true">
    <line x1="4" y1="4" x2="4" y2="102" stroke="var(--lime)" stroke-width="2"/>
    <circle cx="4" cy="4" r="3.5" fill="var(--lime)"/>
    <circle cx="4" cy="36" r="3.5" fill="var(--lime)"/>
    <circle cx="4" cy="68" r="3.5" fill="var(--lime)"/>
    <circle cx="4" cy="102" r="3.5" fill="var(--lime)"/>
  </svg>

  <div class="abs cash-tag">Receive cash by</div>
  <div class="abs cash-dash"></div>

  <div class="abs payout-rail"></div>
  <ul class="abs payout-list">
    <li>
      <span class="payout-icon">
        <svg width="20" height="20" viewBox="0 0 20 20" aria-hidden="true"><circle cx="10" cy="7" r="5" fill="none" stroke="#fff" stroke-width="1.6"/><path d="M2 15h6l3 2 7-4" fill="none" stroke="#fff" stroke-width="1.6" stroke-linecap="round"/></svg>
      </span>Lump Sum
    </li>
    <li>
      <span class="payout-icon">
        <svg width="20" height="20" viewBox="0 0 20 20" aria-hidden="true"><rect x="2" y="5" width="16" height="11" rx="2" fill="none" stroke="#fff" stroke-width="1.6"/><line x1="2" y1="9" x2="18" y2="9" stroke="#fff" stroke-width="1.6"/></svg>
      </span>Monthly Installments
    </li>
    <li>
      <span class="payout-icon">
        <svg width="20" height="20" viewBox="0 0 20 20" aria-hidden="true"><rect x="3" y="4" width="14" height="13" rx="1.5" fill="none" stroke="#fff" stroke-width="1.6"/><line x1="3" y1="8" x2="17" y2="8" stroke="#fff" stroke-width="1.6"/><line x1="7" y1="2" x2="7" y2="5" stroke="#fff" stroke-width="1.6"/><line x1="13" y1="2" x2="13" y2="5" stroke="#fff" stroke-width="1.6"/></svg>
      </span>Line of Credit!!
    </li>
  </ul>

  <div class="abs cta-tag">Call us today</div>
  <div class="abs cta-note">for a Free Consultation!!</div>
  <div class="abs cta-phone">
    <svg width="26" height="26" viewBox="0 0 26 26" aria-hidden="true"><circle cx="13" cy="13" r="13" fill="var(--navy)"/><path d="M9 7l3 3-1.5 2a8 8 0 0 0 4 4l2-1.5 3 3-2 2c-5 0-10.5-5.5-10.5-10.5z" fill="#fff"/></svg>
    (800) 471-2965
  </div>

  <div class="abs contact">
    <div class="contact-row">
      <svg width="14" height="18" viewBox="0 0 14 18" aria-hidden="true"><path d="M7 1a6 6 0 0 1 6 6c0 4-6 10-6 10S1 11 1 7a6 6 0 0 1 6-6z" fill="#fff"/><circle cx="7" cy="7" r="2.2" fill="var(--teal)"/></svg>
      <span>Bluegate Financial Services, Inc.<br>NMLS #318760</span>
    </div>
    <div class="contact-row">
      <svg width="14" height="14" viewBox="0 0 14 14" aria-hidden="true"><g fill="none" stroke="#fff" stroke-width="1.2"><circle cx="7" cy="7" r="6"/><ellipse cx="7" cy="7" rx="2.6" ry="6"/><line x1="1" y1="7" x2="13" y2="7"/></g></svg>
      <span>www.bluegatehome.com</span>
    </div>
  </div>
</div>
</body>
</html>
```